Website for new slot-booking/reservations website/software

For a new software product we need a brand new logo and website for a reservations/booking system. The website should ideally present the main features with information text, contact info, news page as well as registration and pricing pages. As currently primary field of operation the software should be used for tennis but later on, also for other sport types. Also we'd like to be the logo a text-brand which includes the name "feldreserva.net" or just "feldreserva". The logo should ideally include an icon-design in some way. Generally we are open for ideas.

Bootstrap 4 template is a minimum requirement. (Multi-Page preferred, Single-Page still OK.)

You can use the attached image as an inspiration, but change of colors or other design elements are up to you. Currently the application has a primary color of #5500ff. The website created by you will not include the application itself, so it can have different (but ideally similar) Look&Feel.

Target Market(s)

Sports, Club-Management

Logo Text

feldreserva.net

Coding

Coded - Design and coding required

Number of Pages Required

5+ page

Font styles to use
Sans Serif

Requirements
Must have
• Bootstrap 4 Template, SCSS
Nice to have
• Rapid Loading Times, not too much external JS Libraries.
Should not have
• Extensive animations

```html
<!DOCTYPE html>
<html lang="en">
<head>
<meta charset="utf-8">
<title>Feldreserva – Court Booking</title>
<link rel="stylesheet" href="https://fonts.googleapis.com/css2?family=Montserrat:wght@400;500;600;700;800&family=Lora:ital@1&display=swap">
<style>
:root{
  --brand:#5500ff;
  --ink:#2b2b2b;
  --muted:#777;
  --line:#e2e2e2;
  --paper:#ffffff;
  --section:#eeeeee;
  --map:#2c2c2c;
  --court:#2d5a8a;
}
*{box-sizing:border-box;margin:0;padding:0}
html,body{width:760px;height:1200px;overflow:hidden;background:var(--paper)}
body{position:relative;font-family:'Montserrat',sans-serif;color:var(--ink)}
.abs{position:absolute}
.caps{text-transform:uppercase;letter-spacing:.18em}

/* top utility bar */
.utility{left:536px;top:0;width:166px;height:24px;background:var(--brand);display:flex;align-items:center;color:#fff;font-size:7px;font-weight:600}
.utility .search{width:26px;height:100%;display:flex;align-items:center;justify-content:center;border-right:1px solid rgba(255,255,255,.25)}
.utility .lang{width:42px;height:100%;display:flex;align-items:center;justify-content:center;gap:4px;border-right:1px solid rgba(255,255,255,.25)}
.utility .login{flex:1;display:flex;align-items:center;justify-content:center;gap:6px}

/* brand */
.brand{display:flex;align-items:center;gap:5px;color:var(--brand);font-weight:800;letter-spacing:.04em}
.brand .mark{background:var(--brand);display:block}
.header-brand{left:74px;top:41px;font-size:13px}
.header-brand .mark{width:9px;height:9px}

/* nav */
.main-nav{left:276px;top:39px;display:flex;gap:7px}
.main-nav a{width:100px;height:22px;border-top:1px solid var(--line);border-bottom:1px solid var(--line);display:flex;align-items:center;justify-content:center;font-size:6.5px;color:#444;text-decoration:none;letter-spacing:.2em}

/* hero */
.hero{left:0;top:83px;width:760px;height:321px;background:linear-gradient(180deg,#8d8f8a 0%,#3f6f98 28%,#2f5d8d 60%,#22568f 100%)}
.hero-title{left:59px;top:211px;color:#fff;font-size:21px;font-weight:600;letter-spacing:.12em}
.hero-rule{left:59px;top:245px;width:47px;height:1px;background:#fff}
.hero-price{left:59px;top:256px;color:#fff;font-family:'Lora',serif;font-style:italic;font-size:11px}

.field{left:543px;width:154px;height:59px;background:#fff;padding:10px 12px}
.field .label{font-size:6.5px;font-weight:500;letter-spacing:.2em;color:#333}
.field .value{display:flex;align-items:center;margin-top:6px;gap:10px}
.field .big{font-size:20px;font-weight:400;color:#333;letter-spacing:.02em}
.field .serif{font-family:'Lora',serif;font-style:italic;font-size:9px;color:#444}
.field .cal{margin-left:auto}
.date{top:153px}
.time{top:218px}
.btn-outline{left:543px;top:283px;width:154px;height:27px;border:1px solid #fff;color:#fff;display:flex;align-items:center;justify-content:center;font-size:6.5px;font-weight:700;letter-spacing:.2em}
.btn-reserve{left:543px;top:316px;width:154px;height:27px;background:var(--brand);color:#fff;display:flex;align-items:center;justify-content:center;gap:6px;font-size:6.5px;font-weight:700;letter-spacing:.2em}

/* facilities */
.facilities{left:0;top:404px;width:760px;height:333px;background:var(--section)}
.card{top:441px;height:101px;color:#fff;text-align:center}
.card .plus{position:absolute;right:0;top:0;width:24px;height:24px;background:#fff;color:#c9b99a;font-size:12px;display:flex;align-items:center;justify-content:center;font-weight:300}
.card h3{position:absolute;left:0;right:0;top:30px;font-size:7.5px;font-weight:600;letter-spacing:.2em}
.card .rule{position:absolute;left:50%;top:46px;width:18px;height:1px;margin-left:-9px;background:rgba(255,255,255,.6)}
.card p{position:absolute;left:0;right:0;top:53px;font-size:6.2px;line-height:1.4}
.card-tennis{left:59px;width:155px;background:linear-gradient(180deg,#2a3a26 0%,#4d6a3a 65%,#b85a3a 100%)}
.card-football{left:226px;width:148px;background:linear-gradient(180deg,#16283a 0%,#24384a 65%,#2f6b32 100%)}
.card-baseball{left:386px;width:148px;background:linear-gradient(180deg,#1e2a22 0%,#37533a 60%,#8a5a44 100%)}
.card-golf{left:546px;width:154px;background:linear-gradient(180deg,#6e9ac7 0%,#79a86a 45%,#4f9a2c 100%)}

/* promo */
.promo{left:59px;top:577px;width:315px;height:119px;background:linear-gradient(160deg,#3a4335 0%,#57665a 45%,#6d7f76 100%);color:#fff}
.promo .tag{position:absolute;left:0;top:0;width:140px;height:23px;background:var(--brand);display:flex;align-items:center;padding-left:16px;font-size:7.5px;font-weight:600;letter-spacing:.2em}
.promo .from{position:absolute;right:15px;top:15px;text-align:right;font-size:6.2px;font-weight:600;letter-spacing:.1em}
.promo .from strong{display:block;font-size:14px;letter-spacing:0;margin-top:2px}
.promo h4{position:absolute;left:19px;top:44px;font-size:8px;font-weight:600;letter-spacing:.2em}
.promo .rule{position:absolute;left:19px;top:62px;width:18px;height:1px;background:rgba(255,255,255,.7)}
.promo .place{position:absolute;left:19px;top:68px;font-family:'Lora',serif;font-style:italic;font-size:8px}
.promo .book{position:absolute;right:0;bottom:0;width:101px;height:24px;background:#fff;color:var(--brand);display:flex;align-items:center;justify-content:center;gap:16px;font-size:6px;letter-spacing:.2em}

.member{left:386px;top:577px;width:314px;height:119px;background:#fff;text-align:center}
.member h4{margin-top:32px;font-size:8px;font-weight:600;letter-spacing:.15em;color:#333}
.member .rule{width:18px;height:1px;background:var(--line);margin:8px auto 10px}
.member p{font-size:6.2px;line-height:1.75;color:#444;padding:0 58px}
.member .register{position:absolute;right:-1px;bottom:0;width:101px;height:24px;background:var(--brand);color:#fff;display:flex;align-items:center;justify-content:center;gap:6px;font-size:6.5px;font-weight:700;letter-spacing:.15em}

/* map */
.map{left:0;top:737px;width:760px;height:238px;background:radial-gradient(ellipse at 45% 45%,#363636 0%,var(--map) 70%)}

/* footer */
.footer-brand{left:0;right:0;top:1018px;justify-content:center;font-size:19px}
.footer-brand .mark{width:13px;height:13px}
.social{left:0;right:0;top:1074px;display:flex;justify-content:center;gap:24px}
.social span{width:8px;height:8px;border-radius:50%;background:#8a8a8a;display:block}
.footer-nav{left:0;right:0;top:1104px;display:flex;justify-content:center;gap:19px;font-size:6.3px;color:#777;letter-spacing:.2em}
.copyright{left:0;right:0;top:1138px;text-align:center;font-size:5.5px;color:#777;letter-spacing:.12em}
.base{left:0;top:1196px;width:760px;height:4px;background:var(--section)}
</style>
</head>
<body>

<div class="abs utility">
  <div class="search"><svg width="9" height="9" viewBox="0 0 10 10"><circle cx="4.2" cy="4.2" r="3.2" fill="none" stroke="#fff" stroke-width="1.1"/><line x1="6.6" y1="6.6" x2="9.2" y2="9.2" stroke="#fff" stroke-width="1.1"/></svg></div>
  <div class="lang">ENG <svg width="5" height="4" viewBox="0 0 6 4"><path d="M0.5 0.5L3 3L5.5 0.5" fill="none" stroke="#fff"/></svg></div>
  <div class="login caps"><svg width="8" height="8" viewBox="0 0 10 10"><circle cx="5" cy="3" r="2.2" fill="none" stroke="#fff"/><path d="M1 9.5C1 7 3 6 5 6S9 7 9 9.5Z" fill="none" stroke="#fff"/></svg>Member Login</div>
</div>

<div class="abs brand header-brand"><span class="mark"></span>FELDRESERVA</div>

<nav class="abs main-nav">
  <a href="#">ABOUT US</a><a href="#">FACILITIES</a><a href="#">MEMBERSHIP</a><a href="#">CONTACT</a>
</nav>

<div class="abs hero" role="img" aria-label="Photo of an indoor blue tennis court under a dome roof"></div>
<div class="abs hero-title">TENNIS YARD</div>
<div class="abs hero-rule"></div>
<div class="abs hero-price">$30 / hour</div>

<div class="abs field date">
  <div class="label">BOOKING DATE</div>
  <div class="value"><span class="big">27</span><span class="serif">June 2021</span>
    <svg class="cal" width="10" height="9" viewBox="0 0 10 9"><rect x="0.5" y="1.5" width="9" height="7" fill="none" stroke="#444"/><line x1="0.5" y1="3.5" x2="9.5" y2="3.5" stroke="#444"/><path d="M2 5h1M4.5 5h1M7 5h1M2 7h1M4.5 7h1M7 7h1" stroke="#444"/></svg></div>
</div>
<div class="abs field time">
  <div class="label">TIME</div>
  <div class="value"><span class="big">12 : 20</span><span class="serif">AM</span>
    <svg class="cal" width="10" height="9" viewBox="0 0 10 9"><rect x="0.5" y="1.5" width="9" height="7" fill="none" stroke="#444"/><line x1="0.5" y1="3.5" x2="9.5" y2="3.5" stroke="#444"/><path d="M2 5h1M4.5 5h1M7 5h1M2 7h1M4.5 7h1M7 7h1" stroke="#444"/></svg></div>
</div>
<div class="abs btn-outline">LOGIN</div>
<div class="abs btn-reserve">RESERVE NOW <svg width="8" height="6" viewBox="0 0 8 6"><path d="M0 3H7M4.5 0.5L7 3L4.5 5.5" fill="none" stroke="#fff"/></svg></div>

<div class="abs facilities"></div>

<div class="abs card card-tennis" role="img" aria-label="Photo of a tennis player on a clay court">
  <span class="plus">+</span><h3>TENNIS</h3><span class="rule"></span><p>Donec pulvinar,<br>sapien eu posuere</p>
</div>
<div class="abs card card-football" role="img" aria-label="Photo of a floodlit football stadium at night">
  <span class="plus">+</span><h3>FOOTBALL</h3><span class="rule"></span><p>Donec pulvinar,<br>sapien eu posuere</p>
</div>
<div class="abs card card-baseball" role="img" aria-label="Photo of a baseball batter at home plate">
  <span class="plus">+</span><h3>BASEBALL</h3><span class="rule"></span><p>Donec pulvinar,<br>sapien eu posuere</p>
</div>
<div class="abs card card-golf" role="img" aria-label="Photo of a golf ball on a green fairway">
  <span class="plus">+</span><h3>GOLF</h3><span class="rule"></span><p>Donec pulvinar,<br>sapien eu posuere</p>
</div>

<div class="abs promo" role="img" aria-label="Photo of a tennis net on a green court">
  <div class="tag">PROMO OF THE WEEK</div>
  <div class="from">STARTS FROM<strong>$450</strong></div>
  <h4>FOOTBALL FIELD</h4>
  <span class="rule"></span>
  <div class="place">Name of Place</div>
  <div class="book">BOOK NOW <svg width="8" height="7" viewBox="0 0 10 9"><rect x="0.5" y="1.5" width="9" height="7" fill="none" stroke="#5500ff"/><line x1="0.5" y1="3.5" x2="9.5" y2="3.5" stroke="#5500ff"/></svg></div>
</div>

<div class="abs member">
  <h4>BECOME MEMBER</h4>
  <div class="rule"></div>
  <p>Donec pulvinar, sapien eu posuere ullamcorper, enim sapien feugiat nibh, semper posuere tortor augue quis dolor. Integer semper ullamcorper turpis.</p>
  <div class="register">REGISTER NOW <svg width="8" height="6" viewBox="0 0 8 6"><path d="M0 3H7M4.5 0.5L7 3L4.5 5.5" fill="none" stroke="#fff"/></svg></div>
</div>

<div class="abs map" role="img" aria-label="Dark map of Europe and Asia showing club locations"></div>
<svg class="abs" style="left:0;top:737px" width="760" height="238" viewBox="0 0 760 238">
  <g fill="none" stroke="#5500ff" stroke-width="3">
    <circle cx="171" cy="43" r="8.5"/><circle cx="255" cy="53" r="8.5"/><circle cx="117" cy="131" r="8.5"/><circle cx="611" cy="35" r="8.5"/>
  </g>
  <g fill="#5500ff">
    <path d="M167 52L171 62L175 52Z"/><path d="M251 62L255 72L259 62Z"/><path d="M113 140L117 150L121 140Z"/><path d="M607 44L611 54L615 44Z"/>
  </g>
</svg>

<div class="abs brand footer-brand"><span class="mark"></span>FELDRESERVA</div>
<div class="abs social" aria-label="Social links"><span></span><span></span><span></span></div>
<div class="abs footer-nav"><span>ABOUT US</span><span>MEMBERSHIP</span><span>FACILITIES</span><span>CONTACT US</span></div>
<div class="abs copyright">COPYRIGHT © ALL RIGHTS RESERVED BY FELDRESERVA</div>
<div class="abs base"></div>

</body>
</html>
```